Providing Back Office Solutions to Financial Advisors and Attorney Needs a Business Card Design

Need a Business Card Design that speaks to Financial Advisor and Attorneys. Some of the word that come to mind is Clean/Simple & Futuristic.

Industry/Entity Type

Business

```html
<!DOCTYPE html>
<html lang="en">
<head>
<meta charset="utf-8">
<title>Corvane Business Card</title>
<link href="https://fonts.googleapis.com/css2?family=Open+Sans:wght@400;600;700&display=swap" rel="stylesheet">
<style>
  :root {
    --backdrop: #3a2a2c;
    --card-white: #ffffff;
    --brand-blue: #1f6fb2;
    --brand-blue-light: #2f9be0;
    --ink: #111418;
    --base-dark: #0c0f13;
    --ghost: #e4e4e4;
  }
  html, body {
    margin: 0;
    padding: 0;
    width: 1200px;
    height: 800px;
    overflow: hidden;
    background: var(--backdrop);
    font-family: "Open Sans", Arial, sans-serif;
  }
  .card {
    position: absolute;
    left: 75px;
    top: 100px;
    width: 1050px;
    height: 600px;
    background: var(--card-white);
    overflow: hidden;
    box-shadow: 0 20px 50px rgba(0,0,0,0.45);
  }
  .card-base {
    position: absolute;
    inset: 0;
  }
  .ghost-mark {
    position: absolute;
    right: 70px;
    top: 40px;
    width: 230px;
    height: 230px;
    background: var(--ghost);
  }
  .brand-lockup {
    position: absolute;
    left: 70px;
    top: 120px;
    display: flex;
    align-items: center;
  }
  .brand-square {
    width: 70px;
    height: 70px;
    background: var(--brand-blue);
  }
  .brand-divider {
    width: 2px;
    height: 100px;
    background: var(--brand-blue);
    margin: 0 14px 0 22px;
  }
  .brand-name {
    font-size: 60px;
    font-weight: 600;
    letter-spacing: 4px;
    color: var(--brand-blue);
    line-height: 1;
  }
  .brand-tagline {
    font-size: 19px;
    font-weight: 400;
    letter-spacing: 1px;
    color: var(--brand-blue);
    margin-top: 8px;
    padding-top: 4px;
    border-top: 1px solid var(--brand-blue);
  }
  .person {
    position: absolute;
    left: 110px;
    top: 300px;
  }
  .person-name {
    font-size: 34px;
    font-weight: 700;
    color: var(--brand-blue);
    margin: 0;
    line-height: 1.1;
  }
  .person-role {
    font-size: 18px;
    color: var(--ink);
    margin: 4px 0 0 14px;
  }
  .contact-list {
    list-style: none;
    margin: 20px 0 0 30px;
    padding: 0;
  }
  .contact-item {
    display: flex;
    align-items: center;
    font-size: 22px;
    font-weight: 600;
    color: var(--ink);
    height: 32px;
  }
  .contact-icon {
    width: 20px;
    height: 20px;
    margin-right: 16px;
    fill: var(--brand-blue);
  }
</style>
</head>
<body>
  <div class="card">
    <svg class="card-base" width="1050" height="600" viewBox="0 0 1050 600" aria-hidden="true">
      <defs>
        <linearGradient id="stripeBlue" x1="0" y1="0" x2="1" y2="0">
          <stop offset="0" stop-color="#0d4f86"/>
          <stop offset="0.5" stop-color="#2f9be0"/>
          <stop offset="1" stop-color="#1a6fb0"/>
        </linearGradient>
      </defs>
      <path d="M0 585 C 300 560, 650 460, 1050 250 L1050 600 L0 600 Z" fill="url(#stripeBlue)"/>
      <path d="M0 598 C 310 575, 660 478, 1050 268 L1050 600 L0 600 Z" fill="var(--base-dark)"/>
    </svg>

    <div class="ghost-mark" aria-hidden="true"></div>

    <div class="brand-lockup">
      <div class="brand-square" aria-hidden="true"></div>
      <div class="brand-divider" aria-hidden="true"></div>
      <div class="brand-text">
        <div class="brand-name">CORVANE</div>
        <div class="brand-tagline">BACK OFFICE SOLUTIONS</div>
      </div>
    </div>

    <div class="person">
      <h1 class="person-name">Marlo Finch</h1>
      <div class="person-role">Director</div>
      <ul class="contact-list">
        <li class="contact-item">
          <svg class="contact-icon" viewBox="0 0 20 20"><rect x="5" y="1" width="10" height="18" rx="2"/><rect x="7" y="4" width="6" height="8" fill="#fff"/></svg>
          +61 400 555 218
        </li>
        <li class="contact-item">
          <svg class="contact-icon" viewBox="0 0 20 20"><path d="M3 6c0-2 3-3 7-3s7 1 7 3v2h-4V6H7v2H3z"/><rect x="4" y="10" width="12" height="8" rx="1"/></svg>
          +61 7 555 012 34
        </li>
        <li class="contact-item">
          <svg class="contact-icon" viewBox="0 0 20 20"><rect x="1" y="4" width="18" height="12" rx="1"/><path d="M2 5l8 6 8-6" stroke="#fff" stroke-width="1.5" fill="none"/></svg>
          info@corvaneoffice.com
        </li>
        <li class="contact-item">
          <svg class="contact-icon" viewBox="0 0 20 20"><circle cx="10" cy="10" r="9"/><path d="M1 10h18M10 1c-4 4-4 14 0 18M10 1c4 4 4 14 0 18" stroke="#fff" stroke-width="1.2" fill="none"/></svg>
          www.corvaneoffice.com
        </li>
      </ul>
    </div>
  </div>
</body>
</html>
```